Trusty Hound Signage

This design is for "signage" that we intend to get produced.
A couple of different designs that say "Trusty Hound on Guard" and "Beware of Trusty Hound"
It should also have our logo (TH) plus our logo with the hand and dog paw. We would also like the main picture of the sign to be the attached. We would like a classy sophisticated look similar to our logo you designed.
Our designs will go on consumers gates/entrances to warn people there is a dog on the premises. I will get a better quality picture of the dog.
Look and feel
Each slider illustrates characteristics of the customer's brand and the style your logo design should communicate.

```html
<!DOCTYPE html>
<html lang="en">
<head>
<meta charset="utf-8">
<title>Trusty Hound Signage</title>
<link href="https://fonts.googleapis.com/css2?family=Montserrat:wght@400;700&display=swap" rel="stylesheet">
<style>
  :root {
    --backdrop: #4a4849;
    --sign-white: #ffffff;
    --lavender: #9ba9d6;
    --ink: #0a0a0a;
    --dog-dark: #3c3c3c;
    --dog-mid: #565656;
    --shadow-soft: #cfcfcf;
  }
  * { margin: 0; padding: 0; box-sizing: border-box; }
  html, body {
    width: 1200px; height: 1200px; overflow: hidden;
    background: var(--backdrop);
    font-family: "Montserrat", Arial, sans-serif;
  }
  .canvas { position: relative; width: 1200px; height: 1200px; }
  .sign {
    position: absolute; top: 260px; width: 512px; height: 680px;
    background: var(--sign-white);
    box-shadow: 0 2px 6px rgba(0,0,0,0.25);
    overflow: hidden;
  }
  .sign--guard { left: 56px; }
  .sign--beware { left: 632px; }
  .band {
    position: absolute; left: 0; width: 100%;
    background: var(--lavender);
    text-align: center;
  }
  .sign--guard .band { top: 0; height: 196px; }
  .sign--beware .band { bottom: 0; height: 198px; }
  .band-line { display: block; font-weight: 700; line-height: 1; white-space: nowrap; }
  .band-line--name { color: var(--ink); font-size: 54px; }
  .band-line--big { color: var(--sign-white); letter-spacing: -1px; }
  .sign--guard .band-line--name { padding-top: 26px; }
  .sign--guard .band-line--big { font-size: 100px; padding-top: 10px; }
  .sign--beware .band-line--big { font-size: 88px; padding-top: 19px; }
  .sign--beware .band-line--name { padding-top: 22px; }
  .dog-photo {
    position: absolute;
    background: radial-gradient(ellipse at 50% 45%, var(--dog-mid) 0%, var(--dog-dark) 45%, rgba(60,60,60,0) 72%),
                radial-gradient(ellipse at 50% 92%, var(--shadow-soft) 0%, rgba(255,255,255,0) 60%);
  }
  .sign--guard .dog-photo { left: 50px; top: 221px; width: 392px; height: 340px; }
  .sign--beware .dog-photo { left: 51px; top: 125px; width: 392px; height: 340px; }
  .brand {
    position: absolute; display: flex; align-items: center; gap: 10px;
  }
  .sign--guard .brand { left: 65px; top: 583px; }
  .sign--beware .brand { left: 64px; top: 20px; }
  .brand-mark {
    width: 72px; height: 72px; border-radius: 50%;
    border: 3px solid var(--lavender);
  }
  .brand-name {
    font-weight: 400; font-size: 42px; color: var(--ink); white-space: nowrap;
  }
</style>
</head>
<body>
<main class="canvas">
  <section class="sign sign--guard">
    <div class="band">
      <span class="band-line band-line--name">Trusty Hound</span>
      <span class="band-line band-line--big">on Guard</span>
    </div>
    <div class="dog-photo" role="img" aria-label="Photo of a dark low-poly dog sculpture sitting, head turned to the right"></div>
    <div class="brand">
      <div class="brand-mark"></div>
      <span class="brand-name">Trusty Hound</span>
    </div>
  </section>

  <section class="sign sign--beware">
    <div class="brand">
      <div class="brand-mark"></div>
      <span class="brand-name">Trusty Hound</span>
    </div>
    <div class="dog-photo" role="img" aria-label="Photo of a dark low-poly dog sculpture sitting, head turned to the right"></div>
    <div class="band">
      <span class="band-line band-line--big">Beware of</span>
      <span class="band-line band-line--name">Trusty Hound</span>
    </div>
  </section>
</main>
</body>
</html>
```